Emerging automotive detailing business

I am starting a small automotive detailing business in hopes of becoming a well-known detailer to work on high end cars. I would like a card to reflect the high quality and time I put into my work. The name of the company is Brightmere Detailing. I feel like it represents racecars getting off the line at the drag strip as well as an innuendo of "Off the Charts". I do minor paint correction such as clay barring, multi-step buffing and polishing, waxing, hand washes, etc. I am always striving to learn more and improve my work. My goal is to have total customer satisfaction. This is a female run business but I do not want it to be very girly. Elegant is okay! I have pictures of my personal kestrel attached, they do not need to be incorporated but if you can think of a cool way to use 1 or all of them, go for it!

Target Market(s)

Anyone that owns a vehicle. Preferably high end vehicles such as Valdren, Castavelli and Moretto but I will also happily work on any car, truck or suv no matter what brand.

Industry/Entity Type

Automotive

Contact Information for Business Card

Brightmere Detailing
Nora Pellworth
4715 Quillbrook Rd
Red Lion PA 17392
Cell phone- call/text- 717-555-0148
email- brightmeredetails@example.com
Instagram: @brightmeredetailing
Facebook: facebook.example/brightmeredetailing

Requirements
Must have
• Business name, my name, address, phone number. Listing that I do minor paint correction such as clay barring, multi-step buffing and polishing, waxing, hand washes, interior cleaning, and more. (This last part was in nice to haves but I have realized that I do really want it, so I moved it to must haves.) I want something that is different and eye-catching to my customers. Some people have done this very well with cards already submitted to me, but a lot have not. I didn't mess with the "look and feel bars" much because because I am pretty open to the overall design as long as it is not your basic run of the mill design.
Nice to have
• Something car related. Maybe an appointment time/date line. I do not have a logo, but if you would like to design one and incorporate it, that would be amazing!
Should not have
• Purple and Pink colors. Boring, basic, normal card.

```html
<!DOCTYPE html>
<html lang="en">
<head>
<meta charset="utf-8">
<title>Brightmere Detailing – Business Card</title>
<link rel="stylesheet" href="https://fonts.googleapis.com/css2?family=Crimson+Text:wght@400;600&display=swap">
<style>
  :root {
    --backdrop: #e4e2de;
    --card-black: #050505;
    --stripe-gold: #c9ad4c;
    --stripe-khaki: #b9a86a;
    --stripe-bright: #f3d400;
    --name-gold: #f0c92a;
    --text-light: #d9d9d9;
    --card-shadow: rgba(0, 0, 0, 0.28);
  }
  * { box-sizing: border-box; margin: 0; padding: 0; }
  html, body { width: 1200px; height: 873px; overflow: hidden; }
  body {
    background: var(--backdrop);
    font-family: "Crimson Text", Georgia, serif;
    display: flex;
    align-items: center;
    justify-content: center;
    gap: 60px;
  }
  .card {
    position: relative;
    width: 525px;
    height: 320px;
    background: var(--card-black);
    box-shadow: 0 10px 28px var(--card-shadow);
    overflow: hidden;
    display: flex;
    flex-direction: column;
    align-items: center;
    justify-content: center;
    text-align: center;
    color: var(--text-light);
  }
  .stripe-band {
    position: absolute;
    left: 0;
    width: 100%;
    height: 66px;
    background: linear-gradient(to bottom,
      var(--card-black) 0 6px,
      var(--band-gold) 6px 18px,
      var(--card-black) 18px 23px,
      var(--band-gold) 23px 35px,
      var(--card-black) 35px 40px,
      var(--band-gold) 40px 51px,
      var(--card-black) 51px 59px,
      var(--stripe-bright) 59px 62px,
      var(--card-black) 62px 66px);
  }
  .stripe-band--top { top: 0; }
  .stripe-band--bottom { bottom: 0; transform: scaleY(-1); }
  .card--front { --band-gold: var(--stripe-gold); }
  .card--back { --band-gold: var(--stripe-khaki); }

  .business-name {
    font-size: 32px;
    font-weight: 600;
    color: var(--name-gold);
    line-height: 1;
    margin-bottom: 10px;
  }
  .contact-lines {
    list-style: none;
    font-size: 14px;
    line-height: 1.3;
  }
  .services {
    font-size: 16px;
    line-height: 1.3;
    max-width: 330px;
  }
</style>
</head>
<body>
  <section class="card card--front" aria-label="Card front">
    <div class="stripe-band stripe-band--top"></div>
    <h1 class="business-name">Brightmere Detailing</h1>
    <ul class="contact-lines">
      <li>Nora Pellworth</li>
      <li>4715 Quillbrook Rd, Red Lion PA 17392</li>
      <li>Cell phone - call/text - 717-555-0148</li>
      <li>email - brightmeredetails@example.com</li>
      <li>Instagram: @brightmeredetailing</li>
    </ul>
    <div class="stripe-band stripe-band--bottom"></div>
  </section>

  <section class="card card--back" aria-label="Card back">
    <div class="stripe-band stripe-band--top"></div>
    <p class="services">Paint correction<br>such as clay barring, multi-step buffing and polishing, waxing, hand washes, interior cleaning, and more.</p>
    <div class="stripe-band stripe-band--bottom"></div>
  </section>
</body>
</html>
```